We are an Estate agency (Real estate)– looking for Christmas/winter theme leaflet

We are called ‘’HOLLIVERS’’ we are an estate agency based in England. We opened in 2020 in February, few weeks before Covid and we are now known as one of the fastest growing agencies in all of Brighton and Hove.
This is our first Christmas/winter leaflet and this kind of offer!
Offer is: if the client signs with us to sell their home from 1st December 2021 until 7th January 2022 they will receive 50% off HOLLIVERS fees.
I am looking for A5 two-sided leaflet. The first side should contain our branding, the offer. Also, maybe this: ‘’ Let us Treat you this Christmas’’ or maybe on the other side of leaflet, which will contain explanation of the offer, our office details etc. the back should also contain some design.
Our target market is higher end clients who own a property in Brighton and Hove and looking to sell. I would say target market 35+ years of age.
Our branding is clean, fresh and eye catching and that’s what leaflet should look like and represent.
I will insert our website link so you could have a look at the properties that we deal with too. I could also insert last leaflet which I designed and had a really positive response & feedback… maybe will give you some ideas.
I have inserted our brand guidelines. We use Hollivers in white or blue backgrounds as in guideline.
https://www.holliversestateagents.co.uk/
Hi guys,
Thank you for all your ideas so far, however just wanted to mention that I am looking for not so much ''in your face Christmas'' design - something subtle.
Needs to be classy, modern and eye catching - our target market is property owners 35+ years of age. Moreover, this offer needs to be perceived as one off opportunity.
35+ property owners

```html
<!DOCTYPE html>
<html lang="en">
<head>
<meta charset="utf-8">
<title>Hollivers – Christmas Leaflet</title>
<link rel="stylesheet" href="https://fonts.googleapis.com/css2?family=Ubuntu:wght@400;500;700&family=Great+Vibes&display=swap">
<style>
  :root {
    --navy: #012a47;
    --navy-soft: #0a3a5e;
    --pink: #d80f8c;
    --white: #ffffff;
    --backdrop: #a9b5c6;
    --stone: #c9ced3;
    --gift-blue: #2d5fb8;
  }
  * { margin: 0; padding: 0; box-sizing: border-box; }
  html, body {
    width: 886px; height: 1200px; overflow: hidden;
    background: var(--backdrop);
    font-family: "Ubuntu", sans-serif;
  }
  .leaflet-side {
    position: absolute; left: 117px; width: 652px; height: 459px; overflow: hidden;
  }
  /* Front */
  .front { top: 105px; background: var(--navy); }
  .front .winter-pattern {
    position: absolute; inset: 0;
    background: radial-gradient(ellipse at 50% 45%, var(--navy-soft) 0%, var(--navy) 70%);
  }
  .front .house-visual {
    position: absolute; left: 159px; top: 131px; width: 338px; height: 166px;
    background: linear-gradient(180deg, #dfe5ea 0%, var(--stone) 55%, #7b6a58 100%);
    border-radius: 4px;
  }
  .front .brand-name {
    position: absolute; left: 0; right: 0; top: 326px; text-align: center;
    color: var(--white); font-weight: 500; font-size: 34px; letter-spacing: 7px;
  }
  /* Back */
  .back { top: 635px; background: var(--white); color: var(--navy); }
  .headline-lead {
    position: absolute; right: 370px; top: 37px; text-align: right;
    font-size: 26px; line-height: 34px; font-weight: 400;
  }
  .headline-script {
    position: absolute; left: 290px; top: 20px;
    font-family: "Great Vibes", cursive; color: var(--pink);
    font-size: 84px; line-height: 100px;
  }
  .headline-rule {
    position: absolute; left: 270px; top: 122px; width: 129px; height: 5px;
    background: var(--navy); border-radius: 3px;
  }
  .offer-question {
    position: absolute; left: 0; right: 0; top: 146px; text-align: center;
    color: var(--pink); font-weight: 700; font-size: 32px; padding-left: 26px;
  }
  .offer-detail {
    position: absolute; left: 0; right: 0; top: 185px; text-align: center;
    font-size: 24px; padding-left: 26px;
  }
  .offer-detail strong { font-size: 37px; font-weight: 700; letter-spacing: -1px; }
  .offer-dates {
    position: absolute; left: 0; right: 0; top: 236px; text-align: center;
    font-size: 17px; line-height: 22px; padding-left: 26px;
  }
  .gift-visual {
    position: absolute; left: 379px; top: 283px; width: 257px; height: 36px;
    background: linear-gradient(90deg, var(--gift-blue) 0%, #c9d3ea 50%, #1f4f9a 100%);
    border-radius: 6px 6px 0 0;
  }
  .contact-band {
    position: absolute; left: 0; top: 319px; width: 100%; height: 121px;
    background: var(--pink); color: var(--white);
  }
  .contact-band .brand-name {
    position: absolute; left: 121px; top: 46px;
    font-size: 24px; font-weight: 500; letter-spacing: 4px;
  }
  .contact-band .divider {
    position: absolute; left: 309px; top: 17px; width: 1px; height: 82px;
    background: var(--white);
  }
  .contact-list { position: absolute; left: 338px; top: 13px; list-style: none; }
  .contact-list li {
    display: flex; align-items: center; height: 23px;
    font-size: 14.5px; letter-spacing: 0.2px;
  }
  .contact-list svg { width: 16px; height: 16px; margin-right: 10px; flex: none; }
</style>
</head>
<body>
  <section class="leaflet-side front">
    <div class="winter-pattern" role="img" aria-label="Subtle pattern of faint snowflakes on navy"></div>
    <div class="house-visual" role="img" aria-label="3D render of a modern two-storey house with garage"></div>
    <p class="brand-name">HOLLIVERS</p>
  </section>

  <section class="leaflet-side back">
    <p class="headline-lead">Let us treat<br>you this</p>
    <p class="headline-script">Christmas</p>
    <div class="headline-rule"></div>
    <p class="offer-question">Want to Sell your HOME ?</p>
    <p class="offer-detail">Get <strong>50% OFF</strong> on HOLLIVERS fees</p>
    <p class="offer-dates">(from 1st December 2021 until 7th January 2022)</p>
    <div class="gift-visual" role="img" aria-label="Pile of blue and white wrapped Christmas presents with bows"></div>

    <div class="contact-band">
      <p class="brand-name">HOLLIVERS</p>
      <div class="divider"></div>
      <ul class="contact-list">
        <li>
          <svg viewBox="0 0 24 24" fill="none" stroke="#fff" stroke-width="1.5" stroke-linejoin="round"><path d="M5 3h4l2 5-3 2a12 12 0 0 0 6 6l2-3 5 2v4a2 2 0 0 1-2 2A18 18 0 0 1 3 5a2 2 0 0 1 2-2z"/></svg>
          01632 960 418
        </li>
        <li>
          <svg viewBox="0 0 24 24" fill="none" stroke="#fff" stroke-width="1.5"><rect x="3" y="6" width="18" height="12"/><path d="M3 6l9 7 9-7M3 18l7-6M21 18l-7-6"/></svg>
          sales@holliversestateagents.co.uk
        </li>
        <li>
          <svg viewBox="0 0 24 24" fill="none" stroke="#fff" stroke-width="1.5"><circle cx="12" cy="12" r="9"/><ellipse cx="12" cy="12" rx="4" ry="9"/><path d="M3 12h18M5 7h14M5 17h14"/></svg>
          www.holliversestateagents.co.uk
        </li>
        <li>
          <svg viewBox="0 0 24 24" fill="none" stroke="#fff" stroke-width="1.5"><path d="M12 22s7-7 7-12a7 7 0 0 0-14 0c0 5 7 12 7 12z"/><circle cx="12" cy="10" r="2.5"/></svg>
          48 Elm Parade, Hove, BN3 9QZ
        </li>
      </ul>
    </div>
  </section>
</body>
</html>
```